Introducing a Personal Care Product called" ORBA"

We are a nutra-pharmaceutical company launching a new personal care product called ORBA. Some of the products include massage and aroma therapy, as well as personal lubricants. The products will be produced and put into, two bottles that are interlocking so two combinations of products can be purchased at once (i.e. massage and aroma therapy). The poster will be used for promotional advertising, trade shows and for in-store promotions.
Updates

We would like to see a design without the product.

Target Market(s)

Products will be aimed at adults primarily women 18-65 in the USA. We want to appeal to the everyday woman who is interested in their sexual well being.

Industry/Entity Type

Massage

Requirements
Must have
• Clean Presentation. Not many colors. Text should be as follows: ORBA for Her....ORBA for Him...ORBA for You...Let's ORBA see attached..Also ORBA with Her...Orba with Him..Let's ORBA..Open to other copy versions.
Nice to have
• Product image not necessary but can be used. image attached
Should not have
• Too many colors...

```html
<!DOCTYPE html>
<html lang="en">
<head>
<meta charset="utf-8">
<title>NALVA – with her, with him, let's nalva</title>
<link rel="stylesheet" href="https://fonts.googleapis.com/css2?family=Cormorant+Garamond:ital,wght@1,500;1,600&family=Questrial&display=swap">
<style>
  :root {
    --red: #cc0000;
    --blue: #0b1e8e;
    --green: #2ee02a;
    --white: #ffffff;
    --yellow: #ffec00;
    --cyan: #1fe9ff;
    --shadow: rgba(0, 0, 0, 0.45);
  }
  html, body {
    margin: 0;
    padding: 0;
    width: 857px;
    height: 1200px;
    overflow: hidden;
    background: var(--blue);
  }
  .poster {
    display: block;
    width: 857px;
    height: 1200px;
  }
  .band--red { fill: var(--red); }
  .band--blue { fill: var(--blue); }
  .band--green { fill: var(--green); }
  .band-edge { fill: none; stroke: rgba(0, 0, 0, 0.25); stroke-width: 3; }
  .symbol {
    stroke: var(--white);
    fill: none;
    filter: drop-shadow(3px 4px 5px var(--shadow));
  }
  .symbol__fill { fill: var(--white); stroke: none; }
  .headline {
    font-family: "Cormorant Garamond", Georgia, serif;
    font-style: italic;
    font-weight: 600;
    fill: var(--white);
    filter: drop-shadow(2px 3px 4px var(--shadow));
  }
  .headline--closing { font-weight: 500; }
  .connector {
    font-family: "Questrial", "Century Gothic", sans-serif;
    fill: var(--white);
    filter: drop-shadow(2px 3px 4px var(--shadow));
  }
  .pronoun {
    font-family: "Cormorant Garamond", Georgia, serif;
    font-style: italic;
    font-weight: 500;
    filter: drop-shadow(2px 3px 4px var(--shadow));
  }
  .pronoun--her { fill: var(--yellow); }
  .pronoun--him { fill: var(--cyan); }
</style>
</head>
<body>
<svg class="poster" viewBox="0 0 857 1200" xmlns="http://www.w3.org/2000/svg">
  <g role="img" aria-label="Red, blue and green wave bands, each carrying a soft tone-on-tone floral leaf pattern">
    <rect class="band--blue" x="0" y="0" width="857" height="1200"/>
    <path class="band--red" d="M0 0 H857 V322 C710 314 610 370 470 432 C330 492 170 522 0 516 Z"/>
    <path class="band-edge" d="M857 322 C710 314 610 370 470 432 C330 492 170 522 0 516"/>
  </g>

  <g class="symbol">
    <circle cx="598" cy="-20" r="104" stroke-width="24"/>
    <rect class="symbol__fill" x="582" y="92" width="26" height="192"/>
    <rect class="symbol__fill" x="512" y="180" width="168" height="28"/>
  </g>

  <g class="symbol">
    <circle cx="150" cy="780" r="132" stroke-width="24"/>
    <line x1="242" y1="686" x2="392" y2="532" stroke-width="24"/>
    <polygon class="symbol__fill" points="282,489 406,489 406,614 380,614 380,515 282,515"/>
  </g>

  <path class="band--green" d="M0 885 C80 852 170 828 270 834 C430 850 570 990 857 1015 V1200 H0 Z"/>
  <path class="band-edge" d="M0 885 C80 852 170 828 270 834 C430 850 570 990 857 1015"/>

  <text class="headline" x="40" y="190" font-size="190" textLength="375" lengthAdjust="spacingAndGlyphs">nalva</text>
  <text class="connector" x="190" y="272" font-size="56" textLength="116" lengthAdjust="spacingAndGlyphs">with</text>
  <text class="pronoun pronoun--her" x="318" y="320" font-size="150" textLength="205" lengthAdjust="spacingAndGlyphs">her</text>

  <text class="headline" x="432" y="608" font-size="190" textLength="378" lengthAdjust="spacingAndGlyphs">nalva</text>
  <text class="connector" x="480" y="693" font-size="56" textLength="125" lengthAdjust="spacingAndGlyphs">with</text>
  <text class="pronoun pronoun--him" x="540" y="835" font-size="150" textLength="250" lengthAdjust="spacingAndGlyphs">him</text>

  <text class="headline headline--closing" x="60" y="1140" font-size="200" textLength="630" lengthAdjust="spacingAndGlyphs">lets...nalva</text>
</svg>
</body>
</html>
```